professional business card design for technology company

We are a small technology consulting firm, specialising in consulting based around Cloud and Managed services. Our colour scheme is yellow, blue and white, as you can see in the logos. Although we are based in melbourne australia, due to the nature of our work, our clients can be located anywhere. We are looking for a clean, professional, positive look - similar to our company logo

Target Market(s)

small business

Industry/Entity Type

Business

Contact Information for Business Card

eye catching, designed to incorporate some level of raised printing. Must contain website address, phone number, name and job title

Requirements
Must have
• Logo (attached) - use of the same colour scheme

```html
<!DOCTYPE html>
<html lang="en">
<head>
<meta charset="utf-8">
<title>Nubrant Business Card</title>
<link rel="stylesheet" href="https://fonts.googleapis.com/css2?family=Quicksand:wght@500;600;700&family=Teko:wght@600&display=swap">
<style>
  :root {
    --sky: #35a9e1;
    --sky-soft: #72c4ec;
    --charcoal: #58595b;
    --ink: #2f3133;
    --paper: #ffffff;
    --paper-shade: #dedfe0;
    --backdrop: #a9abad;
  }
  * { margin: 0; padding: 0; box-sizing: border-box; }
  html, body { width: 1200px; height: 894px; overflow: hidden; }
  body {
    background: var(--backdrop);
    font-family: "Quicksand", sans-serif;
    display: flex;
    align-items: center;
    justify-content: center;
    gap: 48px;
  }
  .card {
    position: relative;
    width: 540px;
    height: 310px;
    overflow: hidden;
    box-shadow: 0 10px 28px rgba(0,0,0,0.25);
  }

  /* Front */
  .card-front { background: var(--sky); }
  .info-band {
    position: absolute;
    left: 0; right: 0;
    top: 52px; height: 186px;
    border-top: 6px solid var(--charcoal);
    border-bottom: 6px solid var(--charcoal);
    background: radial-gradient(ellipse at 45% 50%, var(--paper) 30%, var(--paper-shade) 100%);
  }
  .name-tab {
    position: absolute;
    left: 0; top: 38px;
    width: 70px; height: 30px;
    background: var(--charcoal);
  }
  .person-name {
    position: absolute;
    left: 82px; top: 28px;
    font-family: "Teko", sans-serif;
    font-weight: 600;
    font-size: 50px;
    line-height: 1;
    color: var(--ink);
    letter-spacing: 1px;
    white-space: nowrap;
  }
  .person-title {
    position: absolute;
    left: 86px; top: 76px;
    font-size: 11px;
    font-weight: 600;
    letter-spacing: 1.5px;
    color: var(--charcoal);
    white-space: nowrap;
  }
  .website-bar {
    position: absolute;
    left: 0; top: 94px;
    width: 250px; height: 22px;
    background: var(--charcoal);
    color: var(--paper);
    font-size: 10.5px;
    font-weight: 500;
    line-height: 22px;
    padding-left: 90px;
    letter-spacing: 0.5px;
    white-space: nowrap;
  }
  .contact-list {
    position: absolute;
    left: 300px; top: 22px;
    list-style: none;
    display: flex;
    flex-direction: column;
    gap: 14px;
  }
  .contact-item {
    display: flex;
    align-items: center;
    gap: 12px;
    font-size: 13px;
    font-weight: 600;
    color: var(--ink);
    line-height: 1.25;
    white-space: nowrap;
  }
  .contact-icon { width: 30px; height: 30px; flex: none; }

  /* Back */
  .card-back { background: var(--sky); }
  .brand-mark {
    position: absolute;
    left: 26px; top: 40px;
    width: 150px; height: 150px;
  }
  .brand-name {
    position: absolute;
    right: 28px; bottom: 14px;
    font-family: "Teko", sans-serif;
    font-weight: 600;
    font-size: 92px;
    line-height: 1;
    color: var(--charcoal);
  }
</style>
</head>
<body>

  <section class="card card-front" aria-label="Business card front">
    <div class="info-band">
      <div class="name-tab"></div>
      <h1 class="person-name">JOHN DOE</h1>
      <p class="person-title">GENERAL MANAGER</p>
      <p class="website-bar">www.nubrant.com</p>

      <ul class="contact-list">
        <li class="contact-item">
          <svg class="contact-icon" viewBox="0 0 30 30" aria-hidden="true">
            <circle cx="15" cy="15" r="15" fill="var(--sky)"/>
            <path d="M8 15 L15 8.5 L22 15 M10.5 13 V21.5 H19.5 V13" fill="none" stroke="#fff" stroke-width="2" stroke-linejoin="round"/>
            <rect x="13.5" y="16.5" width="3" height="5" fill="#fff"/>
          </svg>
          <span>27 Harbour Lane Suite 4<br>Westbay</span>
        </li>
        <li class="contact-item">
          <svg class="contact-icon" viewBox="0 0 30 30" aria-hidden="true">
            <circle cx="15" cy="15" r="15" fill="var(--sky)"/>
            <rect x="10.5" y="7" width="9" height="16" rx="1.5" fill="none" stroke="#fff" stroke-width="1.8"/>
            <circle cx="15" cy="20" r="1" fill="#fff"/>
          </svg>
          <span>014 552 7310</span>
        </li>
        <li class="contact-item">
          <svg class="contact-icon" viewBox="0 0 30 30" aria-hidden="true">
            <circle cx="15" cy="15" r="15" fill="var(--sky)"/>
            <rect x="7.5" y="10" width="15" height="10.5" fill="none" stroke="#fff" stroke-width="1.8"/>
            <path d="M7.5 10 L15 16 L22.5 10" fill="none" stroke="#fff" stroke-width="1.8"/>
          </svg>
          <span>hello@nubrant.com</span>
        </li>
      </ul>
    </div>
  </section>

  <section class="card card-back" aria-label="Business card back">
    <svg class="brand-mark" viewBox="0 0 150 150" role="img" aria-label="Brand mark placeholder">
      <circle cx="75" cy="75" r="70" fill="var(--sky-soft)"/>
    </svg>
    <p class="brand-name">Nubrant</p>
  </section>

</body>
</html>
```